Logistics Website Design

See website https://tvarfreightglobal.com for theme and color details. Need the site to be re-done and reflect some of the designs shown in this list here: https://pinvora.com/tags/logistics-company-website

Target Market(s)

Logistics & Transportation

Industry/Entity Type

Logistics and Supply Chain

Coding

Coded - Design and coding required

Number of Pages Required

5+ page

Requirements
Must have
• Colors must match theme of logo. Looking for a sleek, interactive design.

```html
<!DOCTYPE html>
<html lang="en">
<head>
<meta charset="utf-8">
<title>Tvar Freight Global — Delivering Strength in Every Mile</title>
<link href="https://fonts.googleapis.com/css2?family=Bebas+Neue&family=Inter:wght@400;500;600&family=Orbitron:wght@500&display=swap" rel="stylesheet">
<style>
:root{
  --bg:#1a0b07;
  --bg-2:#24100a;
  --card:#2b140c;
  --orange:#e8673a;
  --orange-soft:#f0946c;
  --peach:#fbe3d6;
  --cream:#f5ece6;
  --muted:#c9b2a6;
  --line:#5a2d1c;
  --ink:#1d0d08;
}
*{box-sizing:border-box;margin:0;padding:0}
html,body{width:1200px;height:5133px;overflow:hidden;background:var(--bg)}
body{font-family:"Inter",sans-serif;color:var(--cream)}
.page{position:relative;width:1200px;height:5133px;overflow:hidden;background:var(--bg)}
.abs{position:absolute}
.display{font-family:"Bebas Neue",sans-serif;font-weight:400;line-height:1}
.label{font-family:"Orbitron",sans-serif;font-size:11px;letter-spacing:3px;color:var(--orange);text-transform:uppercase}
.box-white{background:#fff;color:var(--ink);padding:0 8px;border-radius:3px}
.box-orange{background:var(--orange);color:var(--ink);padding:0 8px;border-radius:3px}
.btn{display:inline-flex;align-items:center;gap:10px;height:40px;padding:0 6px 0 20px;border-radius:20px;background:var(--orange);color:#fff;font-family:"Bebas Neue",sans-serif;font-size:16px;letter-spacing:.5px}
.btn .arrow{width:30px;height:30px;border-radius:50%;border:2px solid #fff;display:grid;place-items:center}
.btn.sm{height:32px;font-size:14px;padding-left:16px}
.btn.sm .arrow{width:24px;height:24px}
.photo{position:absolute}
/* header */
.logo{display:flex;align-items:center;gap:10px}
.logo-dot{width:40px;height:40px;border-radius:50%;background:var(--orange)}
.logo-name{font-family:"Bebas Neue",sans-serif;font-size:26px;color:var(--cream);letter-spacing:1px}
.nav{display:flex;gap:40px;font-family:"Bebas Neue",sans-serif;font-size:15px;letter-spacing:.5px}
.nav span{display:flex;align-items:center;gap:6px}
.hero-p{font-size:15px;line-height:22px;color:var(--muted);border-left:2px solid var(--orange);padding-left:14px;width:490px}
.ghost{background:#fff;color:var(--orange);padding:0 18px 0 6px}
.ghost .arrow{background:var(--orange);border-color:var(--orange)}
/* stats */
.stat{position:absolute;width:200px;text-align:center}
.stat b{display:block;font-family:"Bebas Neue",sans-serif;font-weight:400;font-size:60px;color:var(--cream);line-height:1}
.stat small{font-family:"Bebas Neue",sans-serif;font-size:15px;color:var(--orange)}
.divider{position:absolute;width:1px;height:90px;background:var(--line)}
/* services */
.svc{position:absolute;top:1666px;width:258px;height:410px;background:var(--card);overflow:hidden}
.svc .img{position:absolute;inset:0 0 auto 0;height:200px}
.svc .body{position:absolute;left:0;right:0;top:160px;bottom:0;background:var(--card);clip-path:polygon(0 40px,50% 0,100% 40px,100% 100%,0 100%);text-align:center;padding-top:50px}
.svc h3{font-family:"Bebas Neue",sans-serif;font-weight:400;font-size:22px;line-height:22px;margin-top:10px}
.svc p{font-size:11px;line-height:17px;color:var(--muted);width:200px;margin:10px auto 14px}
.svc.active{border:2px solid var(--orange)}
/* why */
.why-item h4{font-family:"Bebas Neue",sans-serif;font-weight:400;font-size:24px;line-height:26px}
.why-item p{font-size:11px;line-height:18px;color:var(--muted);margin-top:8px}
.why-icon{position:absolute;width:96px;height:96px;border-radius:50%;border:3px solid var(--orange);background:var(--bg-2);display:grid;place-items:center}
/* industries */
.ind{position:absolute;top:3130px;width:194px;height:170px;background:var(--ink);border-radius:4px;text-align:center;padding-top:38px}
.ind .ico{width:56px;height:56px;border-radius:6px;background:var(--orange);margin:0 auto;display:grid;place-items:center}
.ind span{display:block;font-family:"Bebas Neue",sans-serif;font-size:17px;margin-top:18px;color:var(--cream)}
/* testimonials */
.quote-card{position:absolute;top:3542px;width:324px;height:308px;border:1px solid var(--line);border-radius:6px;padding:30px 36px}
.quote-card p{font-size:12px;line-height:23px;color:var(--muted);margin-top:16px}
.person{display:flex;align-items:center;gap:12px;margin-top:18px}
.avatar{width:38px;height:38px;border-radius:50%;background:linear-gradient(135deg,#8c5a44,#3b1e13)}
.person b{font-size:13px;font-weight:600;display:block}
.stars{color:var(--orange);font-size:11px;letter-spacing:2px}
.round{width:30px;height:30px;border-radius:50%;border:2px solid var(--orange);display:grid;place-items:center;color:var(--orange)}
/* form */
.field{position:absolute;height:50px;border:1px solid var(--line);background:rgba(0,0,0,.25);border-radius:3px;display:flex;align-items:center;gap:10px;padding:0 20px;font-size:12px;color:var(--muted)}
/* footer */
.foot-nav li{list-style:none;display:flex;align-items:center;gap:22px;height:52px;border-bottom:1px solid var(--line);font-family:"Bebas Neue",sans-serif;font-size:22px}
.foot-svc li{list-style:none;font-family:"Bebas Neue",sans-serif;font-size:20px;color:var(--muted);height:36px}
.foot-svc li::before{content:"» ";color:var(--orange)}
.foot-h{font-family:"Bebas Neue",sans-serif;font-size:24px}
.social{width:34px;height:34px;border-radius:50%;background:var(--orange)}
</style>
</head>
<body>
<div class="page">

<!-- HERO -->
<div class="photo" role="img" aria-label="White semi truck driving on a highway at dusk" style="left:0;top:0;width:1200px;height:600px;background:linear-gradient(90deg,#2a120b 0%,#3f1d10 40%,#7a4a34 70%,#4a271a 100%);clip-path:polygon(0 0,100% 0,100% 560px,50% 600px,0 560px)"></div>
<div class="abs" style="left:0;top:520px;width:1200px;height:420px;background:linear-gradient(180deg,var(--bg) 0%,#220e08 70%,#6b2e18 100%);clip-path:polygon(0 60px,50% 0,100% 60px,100% 340px,50% 420px,0 340px)"></div>

<header class="abs" style="left:95px;top:30px;width:1030px;height:80px;display:flex;align-items:center;justify-content:space-between">
  <div class="logo"><span class="logo-dot"></span><span class="logo-name">TVAR FREIGHT</span></div>
  <nav class="nav">
    <span><svg width="12" height="12" viewBox="0 0 12 12"><path d="M1 6 6 1l5 5v5H7V8H5v3H1z" fill="#fff"/></svg>HOME</span>
    <span><svg width="12" height="12" viewBox="0 0 12 12"><circle cx="6" cy="6" r="4" fill="none" stroke="#fff" stroke-width="1.6"/></svg>SERVICES</span>
    <span><svg width="12" height="12" viewBox="0 0 12 12"><path d="M1 11V5l3 2V5l3 2V2h4v9z" fill="#fff"/></svg>INDUSTRIES</span>
    <span><svg width="12" height="12" viewBox="0 0 12 12"><circle cx="6" cy="4" r="2.5" fill="none" stroke="#fff" stroke-width="1.3"/><path d="M1.5 11.5c0-3 9-3 9 0" fill="none" stroke="#fff" stroke-width="1.3"/></svg>ABOUT US</span>
    <span><svg width="12" height="12" viewBox="0 0 12 12"><path d="M2 1h3l1 3-2 1c1 2 2 3 3 3l1-2 3 1v3c-6 0-9-3-9-9z" fill="#fff"/></svg>CONTACT US</span>
  </nav>
  <span class="btn">REQUEST A QUOTE <span class="arrow">↗</span></span>
</header>

<h1 class="abs display" style="left:100px;top:210px;font-size:64px;color:#fff">
  <span class="box-white">DELIVERING</span> STRENGTH<br><span style="display:block;margin-top:10px;padding-left:6px">IN EVERY MILE</span>
</h1>
<p class="abs hero-p" style="left:104px;top:362px">We deliver a comprehensive range of open-deck and specialized transportation services—including flatbed, step deck, heavy haul, and over-dimensional freight solutions.</p>
<div class="abs" style="left:102px;top:462px;display:flex;gap:12px">
  <span class="btn">REQUEST A QUOTE <span class="arrow">↗</span></span>
  <span class="btn ghost"><span class="arrow" style="color:#fff">☏</span>CALL US NOW</span>
</div>

<!-- STATS -->
<div class="stat" style="left:166px;top:740px"><b>250</b><small>LOREM IPSUM DOLOR SIT</small></div>
<div class="divider" style="left:380px;top:740px"></div>
<div class="stat" style="left:394px;top:740px"><b>30K+</b><small>LOREM IPSUM DOLOR SIT</small></div>
<div class="divider" style="left:608px;top:740px"></div>
<div class="stat" style="left:624px;top:740px"><b>260</b><small>LOREM IPSUM DOLOR SIT</small></div>
<div class="divider" style="left:840px;top:740px"></div>
<div class="stat" style="left:856px;top:740px"><b>180</b><small>LOREM IPSUM DOLOR SIT</small></div>

<!-- ABOUT -->
<div class="photo" role="img" aria-label="White box truck driving fast on a highway" style="left:114px;top:1020px;width:452px;height:366px;border-radius:6px;background:linear-gradient(135deg,#c9a691,#8a6452 50%,#5c3b2c)"></div>
<div class="abs" style="left:530px;top:1164px;width:72px;height:72px;border-radius:50%;background:var(--bg);border:3px solid var(--orange);display:grid;place-items:center">
  <svg width="36" height="36" viewBox="0 0 36 36"><circle cx="18" cy="18" r="15" fill="none" stroke="#e8673a" stroke-width="3"/><path d="M14 11l11 7-11 7z" fill="#e8673a"/></svg>
</div>
<div class="abs label" style="left:642px;top:1012px">About Company</div>
<h2 class="abs display" style="left:638px;top:1040px;font-size:54px;color:#fff">KEEPING YOUR SUPPLY<br><span class="box-white" style="display:inline-block;margin-top:10px">CHAIN MOVING</span></h2>
<p class="abs" style="left:638px;top:1190px;width:500px;font-size:15px;line-height:25px;color:var(--muted)">We deliver a comprehensive range of open-deck and specialized transportation services—including flatbed, step deck, heavy haul, and over-dimensional freight solutions. Backed by years of experience, a trusted nationwide carrier network, and a strong safety-first culture, we provide reliable, adaptable logistics support built around the unique requirements of every load.</p>
<div class="abs" style="left:632px;top:1366px"><span class="btn">LEARN MORE <span class="arrow">↗</span></span></div>

<!-- SERVICES -->
<div class="abs" style="left:0;top:1476px;width:1200px;height:724px;background:linear-gradient(90deg,#ffffff 10%,var(--peach) 35%,var(--orange-soft) 75%,#ea7a4f 100%);clip-path:polygon(0 0,100% 0,100% 634px,50% 724px,0 634px)"></div>
<div class="abs label" style="left:0;width:1200px;text-align:center;top:1524px;color:var(--ink)">What We Do</div>
<h2 class="abs display" style="left:0;width:1200px;text-align:center;top:1556px;font-size:54px;color:var(--ink)">OUR <span class="box-orange">SERVICES</span></h2>

<div class="svc" style="left:60px;top:1660px"><div class="img photo" role="img" aria-label="Semi truck hauling a flatbed load" style="background:linear-gradient(180deg,#9fb0b8,#5a6266)"></div>
  <div class="body"><svg width="34" height="30" viewBox="0 0 34 30"><rect x="6" y="4" width="22" height="16" rx="2" fill="#e8673a"/><rect x="4" y="22" width="26" height="4" fill="#e8673a"/></svg><h3>FLATBED<br>TRANSPORTATION</h3><p>From routine shipments to oversized and heavy-haul loads, we handle freight requiring proper</p><span class="btn sm">LEARN MORE <span class="arrow">↗</span></span></div></div>
<div class="svc active" style="left:334px;top:1670px"><div class="img photo" role="img" aria-label="Red step deck trailers parked at a yard" style="background:linear-gradient(180deg,#b8c7d6,#7a5048)"></div>
  <div class="body"><svg width="34" height="30" viewBox="0 0 34 30"><rect x="8" y="2" width="18" height="10" fill="#e8673a"/><rect x="2" y="14" width="30" height="6" fill="#e8673a"/><circle cx="9" cy="25" r="3" fill="#e8673a"/><circle cx="25" cy="25" r="3" fill="#e8673a"/></svg><h3>STEP DECK<br>TRANSPORTATION</h3><p>From routine shipments to oversized and heavy-haul loads, we handle freight requiring proper</p><span class="btn sm">LEARN MORE <span class="arrow">↗</span></span></div></div>
<div class="svc" style="left:608px;top:1670px"><div class="img photo" role="img" aria-label="Dry van truck on a road at sunset" style="background:linear-gradient(180deg,#6b6f80,#c4805a 60%,#3a2a22)"></div>
  <div class="body"><svg width="34" height="30" viewBox="0 0 34 30"><rect x="2" y="4" width="20" height="16" fill="#e8673a"/><path d="M23 10h6l3 5v5h-9z" fill="#e8673a"/><circle cx="9" cy="24" r="3" fill="#e8673a"/><circle cx="27" cy="24" r="3" fill="#e8673a"/></svg><h3>DRY VAN<br>TRANSPORTATION</h3><p>From routine shipments to oversized and heavy-haul loads, we handle freight requiring proper</p><span class="btn sm">LEARN MORE <span class="arrow">↗</span></span></div></div>
<div class="svc" style="left:882px;top:1670px"><div class="img photo" role="img" aria-label="Heavy haul truck carrying construction machinery" style="background:linear-gradient(180deg,#9fb6c9,#8c6a4a 60%,#4d5a3a)"></div>
  <div class="body"><svg width="34" height="30" viewBox="0 0 34 30"><rect x="2" y="12" width="18" height="8" fill="#e8673a"/><path d="M21 6h7l4 7v7H21z" fill="#e8673a"/><circle cx="8" cy="24" r="3" fill="#e8673a"/><circle cx="26" cy="24" r="3" fill="#e8673a"/></svg><h3>HEAVY HAUL<br>TRANSPORTATION</h3><p>From routine shipments to oversized and heavy-haul loads, we handle freight requiring proper</p><span class="btn sm">LEARN MORE <span class="arrow">↗</span></span></div></div>

<!-- WHY CHOOSE US -->
<div class="abs" style="left:598px;top:2190px;width:2px;height:70px;background:var(--orange)"></div>
<div class="abs label" style="left:0;width:1200px;text-align:center;top:2288px">Why We Are</div>
<h2 class="abs display" style="left:0;width:1200px;text-align:center;top:2318px;font-size:54px;color:#fff">WHY <span class="box-white">CHOOSE US</span></h2>

<svg class="abs" style="left:0;top:2400px" width="1200" height="420" viewBox="0 0 1200 420">
  <g fill="none" stroke="#e8673a" stroke-width="3">
    <path d="M154 104v60q0 14 14 14h256"/>
    <path d="M1056 104v60q0 14-14 14H786"/>
    <path d="M154 304v-60q0-14 14-14h256"/>
    <path d="M1056 304v-60q0-14-14-14H786"/>
  </g>
  <g fill="#1a0b07" stroke="#e8673a" stroke-width="3"><circle cx="154" cy="108" r="6"/><circle cx="1056" cy="108" r="6"/><circle cx="154" cy="300" r="6"/><circle cx="1056" cy="300" r="6"/></g>
</svg>

<div class="abs" style="left:456px;top:2472px;width:296px;height:296px;border-radius:50%;background:radial-gradient(circle,#3a1a0e,#1f0d08);border:6px solid var(--orange);display:grid;place-items:center">
  <span class="logo-name" style="font-size:40px">TVAR FREIGHT</span>
</div>

<div class="why-icon" style="left:106px;top:2408px"><svg width="44" height="44" viewBox="0 0 44 44" fill="none" stroke="#fff" stroke-width="2.5"><circle cx="20" cy="22" r="14"/><path d="M20 14v8l5 3"/><circle cx="32" cy="32" r="7" fill="#e8673a" stroke="none"/><path d="M29 32l2 2 4-4"/></svg></div>
<div class="abs why-item" style="left:220px;top:2420px;width:240px"><h4>RELIABLE &amp;<br>ON-TIME DELIVERY</h4><p>We ensure every shipment reaches its destination safely and on schedule.</p></div>

<div class="why-icon" style="left:1008px;top:2408px"><svg width="44" height="44" viewBox="0 0 44 44" fill="none" stroke="#fff" stroke-width="2.5"><circle cx="22" cy="13" r="5"/><circle cx="11" cy="18" r="4"/><circle cx="33" cy="18" r="4"/><path d="M12 34c0-10 20-10 20 0zM4 32c0-6 8-7 8-7M40 32c0-6-8-7-8-7"/></svg></div>
<div class="abs why-item" style="left:734px;top:2420px;width:260px;text-align:right"><h4>EXPERIENCED &amp;<br>PROFESSIONAL TEAM</h4><p>Our logistics experts bring years of industry experience to every shipment.</p></div>

<div class="why-icon" style="left:106px;top:2704px"><svg width="44" height="44" viewBox="0 0 44 44" fill="none" stroke="#fff" stroke-width="2.5"><path d="M14 24c-6-7-6-14 0-16s10 5 0 16z"/><circle cx="14" cy="14" r="3"/><path d="M16 30c8 0 4 6 12 6h10"/><circle cx="36" cy="34" r="3" fill="#e8673a" stroke="none"/></svg></div>
<div class="abs why-item" style="left:220px;top:2680px;width:260px"><h4>GLOBAL NETWORK<br>&amp; REACH</h4><p>With a strong worldwide logistics network, we connect businesses across borders.</p></div>

<div class="why-icon" style="left:1008px;top:2704px"><svg width="44" height="44" viewBox="0 0 44 44" fill="none" stroke="#fff" stroke-width="2.5"><rect x="6" y="12" width="20" height="16"/><path d="M26 18h7l5 6v4H26"/><circle cx="13" cy="32" r="3"/><circle cx="32" cy="32" r="3"/><path d="M10 18h8M10 22h6"/></svg></div>
<div class="abs why-item" style="left:734px;top:2680px;width:260px;text-align:right"><h4>CUSTOMIZED<br>LOGISTICS SOLUTIONS</h4><p>We tailor our services to match your unique shipping and business needs.</p></div>

<!-- INDUSTRIES -->
<div class="abs" style="left:0;top:2880px;width:1200px;height:550px;background:linear-gradient(90deg,#ffffff 10%,var(--peach) 35%,var(--orange-soft) 75%,#ea7a4f 100%);clip-path:polygon(0 120px,50% 0,100% 120px,100% 100%,0 100%)"></div>
<div class="abs label" style="left:0;width:1200px;text-align:center;top:2950px;color:var(--ink)">Who We Serve</div>
<h2 class="abs display" style="left:0;width:1200px;text-align:center;top:2980px;font-size:54px;color:var(--ink)">INDUSTRIES <span class="box-white">WE SERVE</span></h2>

<div class="ind" style="left:92px"><div class="ico"><svg width="28" height="28" viewBox="0 0 28 28"><path d="M4 12h20l-2 12H6z" fill="#fff"/><circle cx="10" cy="7" r="3" fill="#fff"/><circle cx="18" cy="7" r="3" fill="#fff"/></svg></div><span>FOOD &amp; BEVERAGE</span></div>
<div class="ind" style="left:306px;top:3116px;height:208px;background:#2b140c"><div class="ico"><svg width="28" height="28" viewBox="0 0 28 28" fill="none" stroke="#fff" stroke-width="2.2"><path d="M3 5h4l3 13h13l2-9H9"/><circle cx="12" cy="23" r="2"/><circle cx="21" cy="23" r="2"/></svg></div><span>E-COMMERCE &amp; RETAIL</span>
  <div class="abs" style="left:22px;bottom:-14px;width:30px;height:30px;border-radius:50%;background:var(--orange);color:#fff;display:grid;place-items:center;font-size:14px">↗</div></div>
<div class="ind" style="left:518px"><div class="ico"><svg width="28" height="28" viewBox="0 0 28 28"><rect x="6" y="5" width="16" height="18" rx="2" fill="#fff"/><circle cx="14" cy="14" r="4" fill="#e8673a"/></svg></div><span>MANUFACTURING</span></div>
<div class="ind" style="left:730px"><div class="ico"><svg width="28" height="28" viewBox="0 0 28 28"><rect x="7" y="3" width="14" height="22" rx="2" fill="#fff"/><path d="M14 9v8M10 13h8" stroke="#e8673a" stroke-width="2.5"/></svg></div><span>PHARMA &amp; HEALTHCARE</span></div>
<div class="ind" style="left:942px"><div class="ico"><svg width="28" height="28" viewBox="0 0 28 28" fill="#fff"><path d="M14 3 3 9h22z"/><rect x="5" y="11" width="3" height="10"/><rect x="12.5" y="11" width="3" height="10"/><rect x="20" y="11" width="3" height="10"/><rect x="3" y="22" width="22" height="3"/></svg></div><span>GOVERNMENT</span></div>

<!-- TESTIMONIALS -->
<div class="abs label" style="left:120px;top:3550px">Testimonials</div>
<h2 class="abs display" style="left:112px;top:3578px;font-size:58px;line-height:64px;color:#fff">SEE WHAT<br>OUR CUSTOMER<br><span class="box-white">ARE SAYING</span></h2>
<p class="abs" style="left:116px;top:3772px;width:300px;font-size:12px;line-height:20px;color:var(--muted)">Lorem ipsum dolor sit amet, consectetur adipiscing elit, sed do eiusmod tempor incididunt</p>
<div class="abs" style="left:124px;top:3850px;display:flex;gap:18px"><span class="round">←</span><span class="round">→</span></div>

<div class="quote-card" style="left:460px">
  <svg width="60" height="30" viewBox="0 0 60 30"><path d="M0 0h24v20l-8 10H4l6-10H0zM32 0h24v20l-8 10H36l6-10H32z" fill="#5a2d1c"/></svg>
  <p>"Lorem ipsum dolor sit amet, consectetur adipiscing elit, sed do eiusmod tempor incididunt ut labore et dolore magna aliqua. Quis ipsum suspendisse ultrices gravida. Risus commodo viverra maecenas accumsan lacus vel facilisis"</p>
  <div class="person"><span class="avatar" role="img" aria-label="Customer portrait"></span><div><b>Jhon Deo</b><span class="stars">★★★★★</span></div></div>
</div>
<div class="quote-card" style="left:808px">
  <svg width="60" height="30" viewBox="0 0 60 30"><path d="M0 0h24v20l-8 10H4l6-10H0zM32 0h24v20l-8 10H36l6-10H32z" fill="#5a2d1c"/></svg>
  <p>"Lorem ipsum dolor sit amet, consectetur adipiscing elit, sed do eiusmod tempor incididunt ut labore et dolore magna aliqua. Quis ipsum suspendisse ultrices gravida. Risus commodo viverra maecenas accumsan lacus vel facilisis"</p>
  <div class="person"><span class="avatar" role="img" aria-label="Customer portrait"></span><div><b>Jhon Deo</b><span class="stars">★★★★★</span></div></div>
</div>

<!-- REQUEST A QUOTE -->
<div class="abs" style="left:0;top:3940px;width:1200px;height:680px;background:linear-gradient(135deg,#3a180c 0%,#1e0c07 55%,#2a110a 100%)"></div>
<div class="photo" role="img" aria-label="Row of parked semi truck cabs" style="left:90px;top:4036px;width:488px;height:488px;border-radius:50%;border:8px solid #7a3a22;background:linear-gradient(160deg,#d9c3b8,#8f6b5e 55%,#3d2620)"></div>
<div class="abs label" style="left:624px;top:4066px">Contact Us</div>
<h2 class="abs display" style="left:620px;top:4090px;font-size:54px;color:#fff">REQUEST A <span class="box-orange">QUOTE</span></h2>
<div class="field" style="left:620px;top:4176px;width:230px">👤 First Name</div>
<div class="field" style="left:860px;top:4176px;width:230px">👤 Last Name</div>
<div class="field" style="left:620px;top:4238px;width:230px">✉ Email address</div>
<div class="field" style="left:860px;top:4238px;width:230px">☏ Phone</div>
<div class="field" style="left:620px;top:4300px;width:470px;height:110px;align-items:flex-start;padding-top:18px">💬 Message</div>
<div class="abs" style="left:614px;top:4434px"><span class="btn">SEND MESSAGE <span class="arrow">↗</span></span></div>

<!-- FOOTER -->
<div class="abs display" style="left:0;width:1200px;text-align:center;top:4990px;font-size:190px;color:rgba(232,103,58,.08);letter-spacing:8px">TVAR FREIGHT</div>
<div class="abs" style="left:110px;top:4760px"><div class="logo"><span class="logo-dot"></span><span class="logo-name">TVAR FREIGHT</span></div></div>
<div class="abs" style="left:136px;top:4860px;display:flex;gap:14px"><span class="social"></span><span class="social"></span><span class="social"></span></div>

<ul class="abs foot-nav" style="left:372px;top:4700px;width:218px">
  <li><span style="color:var(--orange)">⌂</span>HOME</li>
  <li><span style="color:var(--orange)">☺</span>ABOUT</li>
  <li><span style="color:var(--orange)">▤</span>INDUSTRIES</li>
  <li style="border:0"><span style="color:var(--orange)">☏</span>CONTACT US</li>
</ul>
<div class="abs" style="left:612px;top:4700px;width:1px;height:190px;background:var(--line)"></div>
<div class="abs foot-h" style="left:644px;top:4700px">SERVICES</div>
<ul class="abs foot-svc" style="left:644px;top:4746px">
  <li>FLATBED</li><li>STEP DECK</li><li>DRY VAN</li><li>HEAVY HAUL</li>
</ul>
<div class="abs" style="left:842px;top:4700px;width:1px;height:190px;background:var(--line)"></div>
<div class="abs foot-h" style="left:872px;top:4700px">NEWSLETTER SIGN UP</div>
<div class="field" style="left:872px;top:4746px;width:238px;height:36px;font-size:11px;padding:0 12px">✉ Email address</div>
<div class="abs" style="left:872px;top:4796px;width:238px;height:36px;border-radius:3px;background:var(--orange);display:flex;align-items:center;justify-content:center;font-family:'Bebas Neue',sans-serif;font-size:15px;color:#fff">SUBSCRIBE NOW
  <span class="abs" style="right:8px;top:6px;width:24px;height:24px;border-radius:50%;border:2px solid #fff;display:grid;place-items:center;font-size:12px">↗</span></div>

<div class="abs" style="left:0;top:4990px;width:1200px;height:1px;background:var(--line)"></div>
<p class="abs" style="left:0;width:1200px;text-align:center;top:5018px;font-size:13px;color:var(--muted)">© 2026. An independent agent of Kestrel Haul LLC.</p>
<div class="abs" style="left:1062px;top:5012px;width:22px;height:22px;border-radius:50%;background:var(--orange)"></div>

</div>
</body>
</html>
```